Business card design needed-Cake Decorating

I personalize designer cakes without the designer price. I was thinking about a card design that is a little funky, modern and fun. I am very open to suggestions though

Industry/Entity Type

Business

Contact Information for Business Card

Whirlpop Bakes of Canberra
Ph: Maree Dunstan 0438215947
Email:maree@whirlpopbakesofcanberra.com.au
Website:www.whirlpopbakesofcanberra.com.au
ABN: 47 293815064

```html
<!DOCTYPE html>
<html lang="en">
<head>
<meta charset="utf-8">
<title>Whirlpop Bakes of Canberra – Business Card</title>
<link rel="stylesheet" href="https://fonts.googleapis.com/css2?family=Caudex:ital,wght@1,400&family=Pinyon+Script&family=Cormorant+Garamond:ital,wght@0,500;1,500&family=Lato:wght@300&display=swap">
<style>
  :root {
    --paper: #ffffff;
    --brown: #7a4612;
    --brown-deep: #5a3008;
    --gold: #c9963c;
    --gold-light: #f1d79a;
    --rule-dark: #1c1208;
  }
  html, body {
    margin: 0;
    padding: 0;
    overflow: hidden;
    background: var(--paper);
  }
  .card {
    position: relative;
    width: 1200px;
    height: 741px;
    background: var(--paper);
    overflow: hidden;
  }
  .rule {
    position: absolute;
    left: 89px;
    width: 1078px;
    height: 5px;
    background: linear-gradient(90deg, var(--rule-dark) 0%, var(--gold) 18%, var(--gold-light) 50%, var(--gold) 82%, var(--rule-dark) 100%);
  }
  .rule--top { top: 68px; }
  .rule--bottom { top: 678px; }
  .business-name {
    position: absolute;
    left: 0;
    width: 1282px;
    top: 122px;
    margin: 0;
    text-align: center;
    font-family: "Caudex", serif;
    font-style: italic;
    font-weight: 400;
    font-size: 50px;
    line-height: 1;
    color: var(--brown);
    letter-spacing: 0.5px;
  }
  .cake-illustration {
    position: absolute;
    left: 52px;
    top: 198px;
    width: 406px;
    height: 348px;
    border-radius: 50%;
    background: radial-gradient(ellipse at center, #a85a22 0%, #8a4a18 35%, #e8cf9a 62%, #fbf3e0 100%);
  }
  .abn {
    position: absolute;
    left: 804px;
    top: 243px;
    font-family: "Lato", sans-serif;
    font-weight: 300;
    font-size: 27px;
    line-height: 1;
    color: var(--brown);
  }
  .contact {
    position: absolute;
    right: 88px;
    margin: 0;
    text-align: right;
    white-space: nowrap;
    line-height: 1;
    color: var(--brown);
  }
  .contact--person {
    top: 385px;
    font-family: "Pinyon Script", cursive;
    font-size: 70px;
    color: var(--brown-deep);
  }
  .contact--phone {
    top: 500px;
    font-family: "Cormorant Garamond", serif;
    font-style: italic;
    font-weight: 500;
    font-size: 36px;
  }
  .contact--email {
    top: 563px;
    font-family: "Cormorant Garamond", serif;
    font-style: italic;
    font-weight: 500;
    font-size: 32px;
  }
  .contact--web {
    top: 620px;
    font-family: "Cormorant Garamond", serif;
    font-weight: 500;
    font-size: 40px;
    color: var(--brown-deep);
  }
</style>
</head>
<body>
  <div class="card">
    <div class="rule rule--top"></div>

    <h1 class="business-name">Whirlpop Bakes of Canberra</h1>

    <div class="cake-illustration" role="img" aria-label="Illustration of a three-tier chocolate cake decorated with cream flowers inside an ornate gold oval frame"></div>

    <div class="abn">ABN: 47 293815064</div>

    <p class="contact contact--person">Maree Dunstan</p>
    <p class="contact contact--phone">Phone: 0438215947</p>
    <p class="contact contact--email">maree@whirlpopbakesofcanberra.com.au</p>
    <p class="contact contact--web">www.whirlpopbakesofcanberra.com.au</p>

    <div class="rule rule--bottom"></div>
  </div>
</body>
</html>
```